A Clear Three Step Roadmap For Contractors

We are looking for a one-pager "roadmap" that is similar to the 2nd picture we attached, but much more professional & better... please make it landscape orientation. The logo for this system is attached below, as well.

Our Brand Colors to use:
#f2d582
#303030
#8b8c90

The copy we'd like to use on the flyer:
A Clear Three Step Roadmap that will finally allow you to attract quality customers and win more jobs.

The Keystone Ladder Method is a simple to follow system that was created specifically for Contractors and Blue Collar Business Owners.

When it comes to marketing and growing their business, the majority of Contractors are left confused, frustrated and extremely overwhelmed. Unlike most sales, marketing & training programs that offer a single "piece of the puzzle", we've mapped out each essential step of the puzzle and cut out all of the fluff.

All you have to do is complete each step in the right order and we'll be guiding you along the entire journey!

A ---> B

Blueprint: Get clear on where you're going, define your ideal audience, and finally, master your message.
Step 1: Clarify The Chaos
Step 2: Define Your Customer
Step 3: Master Your Message

Build: Attract quality leads, Build your funnel and Formulate a high-converting follow-up system
Step 4: Develop Lead Generator
Step 5: Construct Your Funnel
Step 6: Formulate the Follow-Up

Breakthrough: Get in front of your ideal customers and rapidly scale your business by driving traffic and becoming the authority in your market
Step 7: Turn-On the Traffic
Step 8: Become the Authority
Step 9: Unlock Your Growth

```html
<!DOCTYPE html>
<html lang="en">
<head>
<meta charset="utf-8">
<title>Keystone Ladder Method</title>
<link href="https://fonts.googleapis.com/css2?family=Lato:ital,wght@0,400;0,700;0,900;1,900&display=swap" rel="stylesheet">
<style>
  :root {
    --gold: #f2d582;
    --gold-deep: #eabd45;
    --gold-pale: #f8e7b3;
    --ink: #303030;
    --road: #1c1c1c;
    --steel: #8b8c90;
    --steel-dark: #6f7073;
    --mist: #e9e9ea;
    --paper: #ffffff;
    --backdrop: #a7a7a8;
  }
  * { box-sizing: border-box; margin: 0; padding: 0; }
  html, body { width: 1200px; height: 1200px; overflow: hidden; }
  body {
    background: radial-gradient(circle at 50% 45%, #b6b6b7 0%, var(--backdrop) 70%);
    font-family: "Lato", Arial, sans-serif;
    color: var(--ink);
    position: relative;
  }
  .flyer {
    position: absolute; left: 36px; top: 202px;
    width: 1126px; height: 794px;
    background: var(--paper);
    box-shadow: 0 4px 18px rgba(0,0,0,.25);
    overflow: hidden;
  }
  .header-shapes { position: absolute; left: 0; top: 0; width: 1126px; height: 308px; }
  .brand { position: absolute; left: 26px; top: 30px; display: flex; align-items: center; gap: 40px; }
  .brand-mark { width: 80px; height: 80px; background: var(--gold); }
  .brand-name { color: var(--ink); font-weight: 900; text-transform: uppercase; line-height: .95; }
  .brand-name .line-top { display: block; font-size: 35px; letter-spacing: .5px; }
  .brand-name .line-main { display: block; font-size: 68px; letter-spacing: 2px; }

  .promise { position: absolute; left: 576px; top: 0; width: 550px; height: 132px; text-align: center; padding-top: 20px; }
  .promise-title {
    display: inline-block; color: var(--gold-deep); font-weight: 900; font-size: 29px;
    text-transform: uppercase; letter-spacing: .5px; padding-bottom: 4px;
    border-bottom: 1px solid var(--gold);
  }
  .promise-sub { color: var(--paper); font-weight: 900; font-size: 19px; text-transform: uppercase; line-height: 1.2; margin-top: 6px; }
  .promise-sub .hl { color: var(--gold-deep); }

  .intro {
    position: absolute; left: 96px; top: 182px; width: 494px;
    font-size: 12.6px; line-height: 16px; text-align: justify; color: var(--ink);
  }
  .phases { position: absolute; left: 594px; top: 143px; width: 520px; list-style: none; }
  .phase { display: flex; align-items: flex-start; gap: 18px; height: 54px; }
  .phase-badge {
    flex: 0 0 34px; height: 34px; border-radius: 50%;
    display: flex; align-items: center; justify-content: center;
    color: var(--paper); font-weight: 900; font-size: 17px;
  }
  .phase-a .phase-badge { background: var(--steel-dark); }
  .phase-b .phase-badge { background: var(--gold); }
  .phase-c .phase-badge { background: var(--gold-deep); }
  .phase-name { font-weight: 900; font-size: 15px; text-transform: uppercase; line-height: 15px; }
  .phase-a .phase-name { color: var(--steel-dark); }
  .phase-b .phase-name { color: var(--gold-deep); }
  .phase-c .phase-name { color: var(--gold-deep); }
  .phase-text { font-size: 12.4px; line-height: 14.5px; color: var(--ink); }

  .route { position: absolute; left: 0; top: 308px; width: 1126px; height: 408px; }
  .route text { font-family: "Lato", Arial, sans-serif; font-weight: 900; text-transform: uppercase; }
  .step-no { font-size: 9.5px; }
  .step-title { font-size: 10.5px; }
  .on-steel { fill: var(--paper); }
  .on-pale { fill: var(--ink); }
  .step-no.on-pale { fill: #c4971d; }
  .on-gold { fill: var(--paper); }
  .lane-label { font-size: 14px; letter-spacing: 1.2px; }
  .lane-label.small { font-size: 11.5px; letter-spacing: .6px; }
  .start-label { font-size: 19px; fill: var(--ink); }

  .closing {
    position: absolute; left: 0; top: 716px; width: 1126px; height: 78px;
    background: var(--steel-dark); color: var(--paper);
    display: flex; align-items: center; justify-content: center;
    font-style: italic; font-weight: 900; font-size: 21px;
  }
</style>
</head>
<body>
<main class="flyer">
  <svg class="header-shapes" viewBox="0 0 1126 308" aria-hidden="true">
    <rect x="0" y="0" width="1126" height="308" fill="var(--mist)"/>
    <polygon points="0,0 576,0 576,132 288,158 0,142" fill="var(--paper)"/>
    <rect x="576" y="0" width="550" height="132" fill="var(--road)"/>
  </svg>

  <div class="brand">
    <span class="brand-mark"></span>
    <h1 class="brand-name"><span class="line-top">Keystone Ladder</span><span class="line-main">Method</span></h1>
  </div>

  <header class="promise">
    <h2 class="promise-title">A Clear 3 Step Roadmap</h2>
    <p class="promise-sub">That will finally allow you to <span class="hl">attract</span><br>quality customers &amp; win more jobs!</p>
  </header>

  <p class="intro">The Keystone Ladder Method is a simple to follow system that was created specifically for Contractors and Blue Collar Business Owners. When it comes to marketing and growing their business, the majority of Contractors are left confused, frustrated and extremely overwhelmed. Unlike most sales, marketing &amp; training programs that offer a single "piece of the puzzle", we've mapped out each essential step of the puzzle and cut out all of the fluff.</p>

  <ul class="phases">
    <li class="phase phase-a"><span class="phase-badge">A</span><div><p class="phase-name">Blueprint:</p><p class="phase-text">Get clear on where you're going, define your ideal audience,<br>and finally, master your message.</p></div></li>
    <li class="phase phase-b"><span class="phase-badge">B</span><div><p class="phase-name">Build:</p><p class="phase-text">Attract quality leads, Build your funnel and Formulate a high-converting<br>follow-up system</p></div></li>
    <li class="phase phase-c"><span class="phase-badge">C</span><div><p class="phase-name">Breakthrough:</p><p class="phase-text">Get in front of your ideal customers and rapidly scale your business<br>by driving traffic and becoming the authority in your market</p></div></li>
  </ul>

  <svg class="route" viewBox="0 0 938 340">
    <defs>
      <linearGradient id="steelFade" x1="0" x2="1">
        <stop offset="0" stop-color="#d6d6d8"/><stop offset="1" stop-color="#aeafb2"/>
      </linearGradient>
      <linearGradient id="paleFade" x1="1" x2="0">
        <stop offset="0" stop-color="#f3dc95"/><stop offset="1" stop-color="#fbf0cf"/>
      </linearGradient>
      <linearGradient id="dawnFade" x1="0" x2="1">
        <stop offset="0" stop-color="#ffffff"/><stop offset="1" stop-color="#f4dc94"/>
      </linearGradient>
    </defs>

    <!-- lane labels -->
    <rect x="0" y="5" width="36" height="105" fill="var(--steel-dark)"/>
    <rect x="0" y="110" width="36" height="110" fill="var(--gold)"/>
    <rect x="0" y="220" width="36" height="115" fill="var(--gold-deep)"/>
    <text class="lane-label" transform="translate(23 57) rotate(-90)" text-anchor="middle" fill="#fff">Blueprint</text>
    <text class="lane-label" transform="translate(23 165) rotate(-90)" text-anchor="middle" fill="var(--ink)">Build</text>
    <text class="lane-label small" transform="translate(22 277) rotate(-90)" text-anchor="middle" fill="#fff">Breakthrough</text>

    <!-- road -->
    <path d="M190 67 H840 A52.5 52.5 0 0 1 840 172 H145 A52.5 52.5 0 0 0 145 277 H800" fill="none" stroke="var(--road)" stroke-width="54"/>

    <!-- start pin -->
    <path d="M155 80 C145 62 133 52 133 35 A22 22 0 1 1 177 35 C177 52 165 62 155 80 Z" fill="#5e5f62"/>
    <circle cx="155" cy="35" r="14" fill="var(--gold)"/>
    <path d="M151 27 H159 V35 H164 L155 44 L146 35 H151 Z" fill="#c4971d"/>
    <text class="start-label" x="80" y="95">Start</text>

    <!-- row 1: blueprint -->
    <polygon points="190,40 395,40 413,67 395,94 190,94 208,67" fill="url(#steelFade)"/>
    <polygon points="395,40 600,40 618,67 600,94 395,94 413,67" fill="#a2a3a6"/>
    <polygon points="600,40 805,40 823,67 805,94 600,94 618,67" fill="var(--steel)"/>

    <text class="step-no on-steel" x="242" y="56">Step 1</text>
    <text class="step-title on-steel" x="242" y="71">Clarify</text>
    <text class="step-title on-steel" x="242" y="84">The Chaos</text>
    <circle cx="370" cy="67" r="17" fill="#fff"/>
    <circle cx="370" cy="67" r="10" fill="var(--gold)" stroke="var(--ink)" stroke-width="1.3"/>
    <circle cx="370" cy="67" r="4" fill="none" stroke="var(--ink)" stroke-width="1.3"/>
    <path d="M370 54 V80 M357 67 H383" stroke="var(--ink)" stroke-width="1.1"/>

    <text class="step-no on-steel" x="437" y="56">Step 2</text>
    <text class="step-title on-steel" x="437" y="71">Define</text>
    <text class="step-title on-steel" x="437" y="84">Your Customer</text>
    <circle cx="575" cy="67" r="17" fill="#fff"/>
    <circle cx="575" cy="61" r="5" fill="var(--gold-deep)"/>
    <path d="M565 78 A10 10 0 0 1 585 78 Z" fill="var(--steel-dark)"/>

    <text class="step-no on-steel" x="643" y="56">Step 3</text>
    <text class="step-title on-steel" x="643" y="71">Master</text>
    <text class="step-title on-steel" x="643" y="84">Your Message</text>
    <circle cx="782" cy="67" r="17" fill="#fff"/>
    <polygon points="772,63 780,63 792,56 792,78 780,71 772,71" fill="var(--gold)" stroke="var(--ink)" stroke-width="1.2"/>
    <path d="M776 71 L779 79" stroke="var(--ink)" stroke-width="2"/>

    <!-- row 2: build -->
    <polygon points="775,145 585,145 567,172 585,199 775,199 757,172" fill="#f3dd99"/>
    <polygon points="585,145 380,145 362,172 380,199 585,199 567,172" fill="#f6e4ad"/>
    <polygon points="380,145 175,145 157,172 175,199 380,199 362,172" fill="url(#paleFade)"/>

    <circle cx="610" cy="172" r="17" fill="#fff"/>
    <path d="M603 164 V172 A7 7 0 0 0 617 172 V164" fill="none" stroke="var(--ink)" stroke-width="5"/>
    <path d="M603 164 V168 M617 164 V168" stroke="var(--gold-deep)" stroke-width="5"/>
    <text class="step-no on-pale" x="648" y="161">Step 4</text>
    <text class="step-title on-pale" x="648" y="176">Develop</text>
    <text class="step-title on-pale" x="648" y="189">Lead Generator</text>

    <circle cx="405" cy="172" r="17" fill="#fff"/>
    <polygon points="394,162 416,162 408,173 408,183 402,180 402,173" fill="var(--gold)" stroke="var(--ink)" stroke-width="1.2"/>
    <text class="step-no on-pale" x="442" y="161">Step 5</text>
    <text class="step-title on-pale" x="442" y="176">Construct</text>
    <text class="step-title on-pale" x="442" y="189">Your Funnel</text>

    <circle cx="205" cy="172" r="17" fill="#fff"/>
    <rect x="195" y="162" width="20" height="20" rx="2" fill="none" stroke="var(--ink)" stroke-width="1.2"/>
    <path d="M199 167 H211 M199 172 H211 M199 177 H211" stroke="var(--steel)" stroke-width="1.5"/>
    <rect x="196" y="170" width="3" height="4" fill="var(--gold-deep)"/>
    <text class="step-no on-pale" x="238" y="161">Step 6</text>
    <text class="step-title on-pale" x="238" y="176">Formulate</text>
    <text class="step-title on-pale" x="238" y="189">The Follow Up</text>

    <!-- row 3: breakthrough -->
    <polygon points="160,250 390,250 408,277 390,304 160,304 178,277" fill="url(#dawnFade)"/>
    <polygon points="390,250 595,250 613,277 595,304 390,304 408,277" fill="#f0cf6f"/>
    <polygon points="595,250 800,250 818,277 800,304 595,304 613,277" fill="var(--gold-deep)"/>

    <text class="step-no on-gold" x="240" y="266">Step 7</text>
    <text class="step-title on-gold" x="240" y="281">Turn On</text>
    <text class="step-title on-gold" x="240" y="294">The Traffic</text>
    <circle cx="365" cy="277" r="17" fill="#fff"/>
    <rect x="355" y="267" width="20" height="18" rx="1.5" fill="none" stroke="var(--ink)" stroke-width="1.2"/>
    <rect x="355" y="267" width="20" height="4" fill="var(--gold-deep)"/>
    <path d="M358 276 H366 M358 280 H372" stroke="var(--steel)" stroke-width="1.5"/>

    <text class="step-no on-gold" x="440" y="266">Step 8</text>
    <text class="step-title on-gold" x="440" y="281">Become</text>
    <text class="step-title on-gold" x="440" y="294">The Authority</text>
    <circle cx="570" cy="277" r="17" fill="#fff"/>
    <polygon points="558,287 570,268 582,287" fill="var(--steel)"/>
    <path d="M570 268 V260" stroke="var(--ink)" stroke-width="1.2"/>
    <polygon points="570,260 578,263 570,266" fill="var(--gold-deep)"/>

    <text class="step-no on-gold" x="645" y="266">Step 9</text>
    <text class="step-title on-gold" x="645" y="281">Unlock</text>
    <text class="step-title on-gold" x="645" y="294">Your Growth!</text>
    <circle cx="775" cy="277" r="17" fill="#fff"/>
    <path d="M775 262 C781 268 781 278 779 284 H771 C769 278 769 268 775 262 Z" fill="#fff" stroke="var(--ink)" stroke-width="1.2"/>
    <circle cx="775" cy="273" r="2.2" fill="var(--gold-deep)"/>
    <path d="M773 286 L775 292 L777 286 Z" fill="var(--gold-deep)"/>

    <!-- summit corner -->
    <polygon points="938,230 938,340 820,340" fill="var(--gold-pale)" role="img" aria-label="Illustration of two climbers helping each other reach a summit flag"/>
  </svg>

  <footer class="closing">All you have to do is complete each step in the right order and we'll be guiding you along the entire journey!</footer>
</main>
</body>
</html>
```